Harrowgate Home Works Sales Flyer

We want a sales flyer that outlines our companies strengths with Kitchen & Bath Remodeling. We would like highlight those aspects while also showcasing our ability to do decks and home additions. We want financing packages to be a big part of the flyer.

Target Market(s)

Residential Customers

Requirements
Must have
• Financing options
Highlight Kitchen & bath remodeling
Less subtle is our decks and home additions
Nice to have
• Keep within our logo colors-we are looking for informative flyers that leave homeowners eager to call us after a meeting

```html
<!DOCTYPE html>
<html lang="en">
<head>
<meta charset="utf-8">
<title>Harrowgate Home Works – Sales Flyer</title>
<link rel="stylesheet" href="https://fonts.googleapis.com/css2?family=Montserrat:wght@300;400;500;600;700;800&family=Roboto:wght@400;500;700&display=swap">
<style>
  :root {
    --orange: #f05a2a;
    --brick: #c9292a;
    --royal: #1a5fae;
    --navy: #0b2343;
    --white: #ffffff;
    --plan-a: #04a6e3;
    --plan-b: #38b54a;
    --plan-c: #93278f;
    --contact-blue: #1c55a4;
  }
  * { margin: 0; padding: 0; box-sizing: border-box; }
  html, body { width: 848px; height: 1200px; overflow: hidden; background: var(--white); }
  .flyer { position: relative; width: 848px; height: 1200px; overflow: hidden; background: var(--white); font-family: "Roboto", sans-serif; }

  .brand { position: absolute; left: 0; top: 0; width: 505px; height: 183px; display: flex; align-items: center; justify-content: center; gap: 10px; }
  .brand-square { width: 16px; height: 16px; background: var(--orange); }
  .brand-name { font-family: "Montserrat", sans-serif; font-weight: 700; font-size: 27px; color: var(--orange); letter-spacing: 0.5px; }

  .kitchen-photo { position: absolute; left: 0; top: 183px; width: 848px; height: 410px;
    background: linear-gradient(180deg, #d8d0c6 0%, #b99873 35%, #a7855f 50%, #e4e4e8 62%, #d4d5da 100%); }

  .hero-panel { position: absolute; left: 505px; top: 0; width: 343px; height: 432px; background: var(--orange); }
  .hero-band { position: absolute; left: 505px; top: 432px; width: 343px; height: 46px; background: var(--brick); }
  .hero-title { position: absolute; left: 533px; top: 158px; color: var(--white); font-family: "Montserrat", sans-serif; }
  .hero-title .bold { display: block; font-weight: 800; font-size: 32px; line-height: 41px; }
  .hero-title .thin { display: block; font-weight: 300; font-size: 42px; line-height: 54px; margin-top: -2px; }
  .hero-copy { position: absolute; left: 533px; top: 314px; width: 300px; color: var(--white); font-family: "Montserrat", sans-serif; font-weight: 500; font-size: 17.5px; line-height: 22px; }

  .services-column { position: absolute; left: 0; top: 570px; width: 302px; height: 630px; background: var(--royal); }
  .bath-photo { position: absolute; left: 0; top: 592px; width: 302px; height: 302px;
    background: linear-gradient(180deg, #eceff2 0%, #dfe2e6 55%, #c9cbcf 100%); }
  .services-title { position: absolute; left: 54px; top: 912px; color: var(--white); font-family: "Montserrat", sans-serif; font-weight: 700; font-size: 18px; }
  .services-list { position: absolute; left: 54px; top: 955px; list-style: none; color: var(--white); font-family: "Montserrat", sans-serif; font-weight: 400; font-size: 23px; line-height: 27px; }
  .services-list li { position: relative; padding-left: 30px; margin-bottom: 12px; }
  .services-list li::before { content: ""; position: absolute; left: 2px; top: 9px; width: 12px; height: 12px; border-radius: 50%; background: var(--white); }

  .plans-area { position: absolute; left: 302px; top: 592px; width: 546px; height: 520px; background: var(--navy); }
  .intro { position: absolute; left: 344px; top: 620px; width: 480px; color: var(--white); font-size: 16.3px; line-height: 20.6px; font-weight: 500; }

  .plan { position: absolute; left: 344px; width: 412px; height: 111px; border: 1.5px solid; display: flex; }
  .plan-a { top: 726px; border-color: var(--plan-a); }
  .plan-b { top: 852px; border-color: var(--plan-b); }
  .plan-c { top: 977px; border-color: var(--plan-c); }
  .plan-price { width: 112px; height: 100%; padding: 11px 0 0 12px; color: var(--white); }
  .plan-a .plan-price { background: var(--plan-a); }
  .plan-b .plan-price { background: var(--plan-b); }
  .plan-c .plan-price { background: var(--plan-c); }
  .plan-name { font-weight: 700; font-size: 18.5px; line-height: 22px; }
  .plan-amount { font-weight: 700; font-size: 30px; line-height: 34px; margin-top: 13px; }
  .plan-unit { font-size: 19px; line-height: 20px; }
  .plan-details { padding: 12px 0 0 14px; color: var(--white); }
  .plan-heading { font-weight: 700; font-size: 17px; line-height: 22px; margin-bottom: 5px; }
  .plan-details p { font-size: 14.5px; line-height: 18px; }

  .contact { position: absolute; left: 302px; top: 1112px; width: 546px; height: 88px; text-align: center; font-family: "Montserrat", sans-serif; color: var(--contact-blue); padding-left: 0; }
  .contact-cta { margin-top: 14px; font-weight: 600; font-size: 17px; }
  .contact-cta strong { color: var(--orange); font-weight: 800; font-size: 19px; }
  .contact-line { margin-top: 6px; font-weight: 400; font-size: 24px; word-spacing: 2px; }
  .contact-line .sep { margin: 0 16px; }
</style>
</head>
<body>
<div class="flyer">
  <header class="brand">
    <span class="brand-square"></span>
    <span class="brand-name">Harrowgate Home Works</span>
  </header>

  <div class="kitchen-photo" role="img" aria-label="Photo of a woman working at a modern kitchen counter with wood shelving and white cabinets"></div>

  <section class="hero-panel"></section>
  <div class="hero-band"></div>
  <h1 class="hero-title">
    <span class="bold">Convert</span>
    <span class="bold">Your Home of</span>
    <span class="thin">Your Dreams!</span>
  </h1>
  <p class="hero-copy">It’s time to convert your kitchen or bathroom and give it the look &amp; functionality you’ve been dreaming of !</p>

  <aside class="services-column"></aside>
  <div class="bath-photo" role="img" aria-label="Photo of a bright white marble bathroom with freestanding tub, basin and round mirror"></div>
  <h2 class="services-title">Our Services</h2>
  <ul class="services-list">
    <li>Kitchens</li>
    <li>Bathrooms</li>
    <li>Decks &amp; Home<br>Additions</li>
    <li>Remodels</li>
    <li>Renovations</li>
  </ul>

  <section class="plans-area"></section>
  <p class="intro">At Harrowgate Home Works, it’s our goal to enhance your quality of life by giving you the home of your dreams through a distinctive kitchen and bath remodeling experience with great financing options.</p>

  <div class="plan plan-a">
    <div class="plan-price"><div class="plan-name">Plan - A</div><div class="plan-amount">000</div><div class="plan-unit">$/Month</div></div>
    <div class="plan-details"><div class="plan-heading">Lorem ipsum dolor sit amet</div><p>Details will be here.</p><p>Details will be here.</p><p>Details will be here.</p></div>
  </div>
  <div class="plan plan-b">
    <div class="plan-price"><div class="plan-name">Plan - B</div><div class="plan-amount">000</div><div class="plan-unit">$/Month</div></div>
    <div class="plan-details"><div class="plan-heading">Lorem ipsum dolor sit amet</div><p>Details will be here.</p><p>Details will be here.</p><p>Details will be here.</p></div>
  </div>
  <div class="plan plan-c">
    <div class="plan-price"><div class="plan-name">Plan - C</div><div class="plan-amount">000</div><div class="plan-unit">$/Month</div></div>
    <div class="plan-details"><div class="plan-heading">Lorem ipsum dolor sit amet</div><p>Details will be here.</p><p>Details will be here.</p><p>Details will be here.</p></div>
  </div>

  <footer class="contact">
    <p class="contact-cta">For <strong>FREE Estimation</strong> Contact us tody!</p>
    <p class="contact-line">+ 000 000 0000<span class="sep">|</span>info@email.com</p>
  </footer>
</div>
</body>
</html>
```